Business Card Design Project

for a second hand vintage clothing store. shop name is The Velvet Cupboard

Cards to be double sided

The name on the card is Joanna Whitfield

Information to put on card:

The Velvet Cupboard
Joanna Whitfield (no job title)
42/871 Dunmore St, Glenwick, Sydney, NSW, 2009.
Mobile: 0412 905 261
Email: thevelvetcupboard@mailbox.com.au
Web: www.thevelvetcupboard.com.au

Target Market(s)

Women looking at vintage clothing

Industry/Entity Type

Clothing

```html
<!DOCTYPE html>
<html lang="en">
<head>
<meta charset="utf-8">
<title>The Velvet Cupboard – Business Card</title>
<link rel="stylesheet" href="https://fonts.googleapis.com/css2?family=Crimson+Text:ital,wght@1,400;1,700&display=swap">
<style>
  :root {
    --canvas: #f3f2f2;
    --plum: #53212f;
    --cream: #f1dd9e;
    --cream-text: #f3e4b4;
  }
  * { margin: 0; padding: 0; box-sizing: border-box; }
  html, body {
    width: 1200px;
    height: 899px;
    overflow: hidden;
    background: var(--canvas);
  }
  .canvas {
    position: relative;
    width: 1200px;
    height: 899px;
  }
  .card {
    position: absolute;
    width: 520px;
    height: 300px;
    background: var(--plum);
    border-radius: 22px;
    overflow: hidden;
    font-family: "Crimson Text", "Times New Roman", serif;
    font-style: italic;
    color: var(--cream-text);
  }
  .card--front { left: 90px; top: 120px; }
  .card--back  { left: 590px; top: 480px; }
  .card__bands {
    position: absolute;
    inset: 0;
    width: 100%;
    height: 100%;
  }
  .card__bands polygon { fill: var(--cream); }

  .wordmark {
    position: absolute;
    left: 0;
    right: 0;
    text-align: center;
    font-weight: 400;
    color: var(--cream-text);
    white-space: nowrap;
  }
  .card--front .wordmark { top: 118px; font-size: 46px; }
  .card--back .wordmark { top: 30px; font-size: 36px; }

  .holder-name {
    position: absolute;
    left: 26px;
    top: 104px;
    font-size: 25px;
    font-weight: 700;
    color: var(--plum);
    white-space: nowrap;
  }
  .address {
    position: absolute;
    left: 26px;
    top: 160px;
    font-size: 15.5px;
    line-height: 1.3;
  }
  .contact {
    position: absolute;
    right: 26px;
    top: 150px;
    font-size: 14.5px;
    line-height: 1.55;
    text-align: right;
  }
</style>
</head>
<body>
<main class="canvas">

  <section class="card card--front" aria-label="Card front">
    <svg class="card__bands" viewBox="0 0 520 300" aria-hidden="true">
      <polygon points="0,0 200,0 172,24 0,24"/>
      <polygon points="372,276 520,276 520,300 348,300"/>
    </svg>
    <p class="wordmark">The Velvet Cupboard</p>
  </section>

  <section class="card card--back" aria-label="Card back">
    <svg class="card__bands" viewBox="0 0 520 300" aria-hidden="true">
      <polygon points="0,0 200,0 172,24 0,24"/>
      <polygon points="0,100 232,100 256,120 232,140 0,140"/>
      <polygon points="372,276 520,276 520,300 348,300"/>
    </svg>
    <p class="wordmark">The Velvet Cupboard</p>
    <p class="holder-name">Joanna Whitfield</p>
    <address class="address">
      42/871 Dunmore St,<br>
      Glenwick, Sydney,<br>
      NSW, 2009.
    </address>
    <p class="contact">
      T : 0412 905 261<br>
      E : thevelvetcupboard@mailbox.com.au<br>
      www.thevelvetcupboard.com.au
    </p>
  </section>

</main>
</body>
</html>
```